Web design project for exciting Australian start-up

Background
We are looking for a creative and talented web design artist to work alongside our market leading web developer.
• You will be required to create a modern and clean design theme for our website, incorporating selected rustic colour scheme elements for our exciting Australian start-up to operate within the coffee industry.
reoccurring work to be expected to flow to the successful designer.
Requirements
• c. 5 - 10 page website
• Landing page
• Log in/ out
• 404 template
• Typography is emphasised
• Please use either a) quillnest.com, b) free web fonts, c) plovra fonts
• All design elements in vector format
• Preferably with icons for each header title(i.e. about us, how it works etc) but designer have free reign over how the site looks, so might not be applicable
• All pages to be responsive
• Down to Kelvo resolution

High level visual design brief attached - additional pages to be worked from base design.

Design inspiration
• We would like to use design elements from the following sources:
http://www.plovra.com/vintel/ (Functionality)
Colour scheme refer to logo and complementary style guide

```html
<!DOCTYPE html>
<html lang="en">
<head>
<meta charset="utf-8">
<title>Bean Meridian — Online Coffee Market Place</title>
<link rel="stylesheet" href="https://fonts.googleapis.com/css2?family=Oswald:wght@500;600&family=Roboto:wght@300;400;500;700&display=swap">
<style>
  :root {
    --orange: #f7932f;
    --ink: #111111;
    --grey-text: #4a4a4a;
    --nav-text: #777777;
    --footer-bg: #e6e6e6;
    --burlap-light: #efe6d6;
    --burlap-mid: #e2d3bb;
    --sack: #b48a63;
    --bean: #b98a66;
    --white: #ffffff;
  }
  * { box-sizing: border-box; margin: 0; padding: 0; }
  html, body { width: 1200px; height: 988px; overflow: hidden; }
  body { position: relative; background: var(--white); font-family: "Roboto", Arial, sans-serif; color: var(--ink); }

  .site-header { position: absolute; top: 0; left: 0; width: 1200px; height: 83px; background: var(--white); }
  .brand { position: absolute; left: 51px; top: 29px; display: flex; align-items: center; gap: 8px;
    font-family: "Roboto", Arial, sans-serif; font-weight: 700; font-size: 20px; letter-spacing: 1px; color: #2b2b2b; }
  .brand-dot { width: 22px; height: 22px; border-radius: 50%; background: var(--orange); }
  .main-nav { position: absolute; right: 53px; top: 28px; display: flex; align-items: center; gap: 34px; }
  .main-nav a { text-decoration: none; color: var(--nav-text); font-size: 13px; letter-spacing: 0.2px; }
  .main-nav .login-button { background: var(--orange); color: var(--white); padding: 7px 14px 7px 12px;
    display: flex; align-items: center; gap: 7px; border: 1px solid #e88420; }

  .hero { position: absolute; top: 83px; left: 0; width: 1200px; height: 707px;
    background: radial-gradient(ellipse at 40% 35%, var(--burlap-light) 0%, var(--burlap-mid) 100%); }
  .hero-sack { position: absolute; left: 725px; top: 112px; width: 370px; height: 410px;
    border-radius: 40px 40px 30px 30px; background: linear-gradient(180deg, #8b6a4f 0%, var(--sack) 25%, #c8a27d 100%); opacity: 0.9; }
  .hero-beans { position: absolute; left: 0; bottom: 0; width: 1200px; height: 200px;
    background: linear-gradient(180deg, rgba(185,138,102,0) 0%, rgba(185,138,102,0.75) 40%, rgba(170,125,92,0.85) 100%); }
  .hero-title { position: absolute; left: 94px; top: 168px; }
  .hero-title .line-light { display: block; font-weight: 300; font-size: 58px; letter-spacing: -3px; color: #444; line-height: 1; }
  .hero-title .line-accent { display: block; font-family: "Oswald", Arial, sans-serif; font-weight: 600; font-size: 76px; color: var(--orange); line-height: 1; margin-top: -2px; }
  .hero-title .line-strong { display: block; font-family: "Oswald", Arial, sans-serif; font-weight: 600; font-size: 64px; color: var(--ink); line-height: 1; margin-top: -6px; }
  .watch-video { position: absolute; left: 94px; top: 379px; width: 189px; height: 43px;
    border: 1px solid #b5b0a8; background: rgba(255,255,255,0.35); display: flex; align-items: center; gap: 16px; padding-left: 24px;
    font-family: "Oswald", Arial, sans-serif; font-weight: 500; font-size: 20px; color: #3a3a3a; text-decoration: none; }

  .site-footer { position: absolute; top: 790px; left: 0; width: 1200px; height: 198px; background: var(--footer-bg); }
  .footer-col { position: absolute; top: 33px; }
  .footer-col h3 { font-weight: 400; font-size: 14px; color: var(--ink); margin-bottom: 15px; letter-spacing: -0.2px; }
  .footer-col p { font-weight: 300; font-size: 12px; line-height: 16.6px; color: var(--grey-text); width: 310px; }
  .footer-col ul { list-style: none; }
  .footer-col li { font-weight: 300; font-size: 13.5px; color: #333; line-height: 20px; }
  .col-about { left: 51px; }
  .col-helpful { left: 428px; }
  .col-who { left: 617px; }
  .col-follow { left: 788px; }
  .col-follow li { display: flex; align-items: center; gap: 9px; line-height: 27px; color: #555; font-size: 14px; }
  .social-dot { width: 18px; height: 18px; border-radius: 50%; background: #8a8a8a; }
  .footer-brand { position: absolute; left: 961px; top: 73px; display: flex; align-items: center; gap: 8px;
    font-weight: 700; font-size: 18px; letter-spacing: 1px; color: #666; }
  .copyright { position: absolute; left: 961px; top: 116px; font-weight: 300; font-size: 13px; color: #444; }
</style>
</head>
<body>
  <header class="site-header">
    <div class="brand"><span class="brand-dot"></span>BEAN MERIDIAN</div>
    <nav class="main-nav">
      <a href="#">HOME</a>
      <a href="#">ABOUT US</a>
      <a href="#">HOW IT WORKS</a>
      <a href="#" class="login-button">
        <svg width="13" height="14" viewBox="0 0 13 14"><circle cx="6.5" cy="4" r="3.5" fill="#fff"/><path d="M0 14c0-4 3-6 6.5-6S13 10 13 14z" fill="#fff"/></svg>
        LOGIN
      </a>
    </nav>
  </header>

  <section class="hero" role="img" aria-label="Burlap texture background with a sack of roasted coffee beans and scattered beans along the bottom">
    <div class="hero-sack"></div>
    <div class="hero-beans"></div>
    <h1 class="hero-title">
      <span class="line-light">AUSTRALIA’S FIRST</span>
      <span class="line-accent">ONLINE COFFEE</span>
      <span class="line-strong">MARKET PLACE</span>
    </h1>
    <a href="#" class="watch-video">
      <svg width="12" height="14" viewBox="0 0 12 14"><path d="M0 0L12 7L0 14z" fill="#f7932f"/></svg>
      WATCH VIDEO
    </a>
  </section>

  <footer class="site-footer">
    <div class="footer-col col-about">
      <h3>ABOUT US</h3>
      <p>Lorem ipsum dolor sit amet, consectetur adipisicing elit, sed do eiusmod tempor incididunt ut labore et dolore magna aliqua. Ut enim ad minim veniam, quis nostrud exercitation ullamco laboris nisi ut aliquip ex ea commodo consequat. Duis aute irure dolor in reprehenderit in voluptate velit esse cillum dolore eu fugiat nulla pariatur.</p>
    </div>
    <div class="footer-col col-helpful">
      <h3>HELPFUL INFO</h3>
      <ul><li>About us</li><li>Media Enquiries</li><li>Terms &amp; Conditions</li><li>Privacy Policy</li></ul>
    </div>
    <div class="footer-col col-who">
      <h3>WHO WE ARE</h3>
      <ul><li>How It Works</li><li>Faq</li><li>Contact Us</li></ul>
    </div>
    <div class="footer-col col-follow">
      <h3>FOLLOW US</h3>
      <ul>
        <li><span class="social-dot"></span>Friendwall</li>
        <li><span class="social-dot"></span>Worklink</li>
        <li><span class="social-dot"></span>Friendwall</li>
        <li><span class="social-dot"></span>Worklink</li>
      </ul>
    </div>
    <div class="footer-brand"><span class="brand-dot"></span>BEAN MERIDIAN</div>
    <div class="copyright">Copyright © 2014 Bean Meridian.</div>
  </footer>
</body>
</html>
```